business card/stationary design
business card/stationary
Use same font as used in my logo
Use different font if you think it looks better
Professional
Glen R. Whitmore
Managing Partner
4197-B West Harlow Creek Rd.
Brenton Falls, OR 97481
glen.whitmore@bluelanternfinancialgroup.example
Bluelanternfinancialgroup.example
I want a clean professional looking card and simple stationary design.
nothing

```html
<!DOCTYPE html>
<html lang="en">
<head>
<meta charset="utf-8">
<title>Blue Lantern Financial Group – Business Card</title>
<link href="https://fonts.googleapis.com/css2?family=Cinzel:wght@600&family=Open+Sans:wght@400;600&display=swap" rel="stylesheet">
<style>
  :root {
    --backdrop: #ebe6e1;
    --card: #ffffff;
    --maroon: #8b2842;
    --maroon-light: #b34a64;
    --gold: #a8893b;
    --text-grey: #555555;
    --title-grey: #7a7a7a;
  }
  html, body {
    margin: 0;
    padding: 0;
    width: 1200px;
    height: 965px;
    overflow: hidden;
    background: var(--backdrop);
  }
  .business-card {
    position: absolute;
    left: 150px;
    top: 247px;
    width: 900px;
    height: 470px;
    background: var(--card);
    border-radius: 28px;
    overflow: hidden;
    box-shadow: 0 6px 18px rgba(0,0,0,0.12);
    font-family: "Open Sans", sans-serif;
  }
  .card-wave {
    position: absolute;
    left: 0;
    top: 0;
    width: 900px;
    height: 470px;
  }
  .brand {
    position: absolute;
    left: 0;
    top: 18px;
    width: 900px;
    text-align: center;
    color: var(--maroon);
    font-family: "Cinzel", serif;
    font-weight: 600;
  }
  .brand-mark {
    display: block;
    width: 62px;
    height: 62px;
    margin: 0 auto 8px;
    border-radius: 50%;
    background: var(--maroon);
  }
  .brand-name {
    display: block;
    font-size: 50px;
    line-height: 56px;
    letter-spacing: 1px;
  }
  .brand-sub {
    display: block;
    font-size: 28px;
    line-height: 34px;
    letter-spacing: 3px;
  }
  .person {
    position: absolute;
    right: 567px;
    top: 262px;
    text-align: right;
  }
  .person-name {
    margin: 0;
    color: var(--maroon);
    font-weight: 600;
    font-size: 24px;
    line-height: 30px;
  }
  .person-title {
    margin: 0;
    color: var(--title-grey);
    font-size: 15px;
    line-height: 22px;
  }
  .divider {
    position: absolute;
    left: 348px;
    top: 232px;
    width: 2px;
    height: 144px;
    background: var(--gold);
  }
  .contact {
    position: absolute;
    left: 364px;
    top: 226px;
    margin: 0;
    padding: 0;
    list-style: none;
    color: var(--text-grey);
    font-size: 17px;
    line-height: 25px;
  }
  .contact-label {
    color: var(--maroon);
    font-weight: 600;
  }
</style>
</head>
<body>
  <div class="business-card">
    <svg class="card-wave" viewBox="0 0 900 470" aria-hidden="true">
      <defs>
        <linearGradient id="bandGradient" x1="0" y1="0" x2="1" y2="0">
          <stop offset="0" stop-color="var(--maroon)"/>
          <stop offset="0.55" stop-color="var(--maroon-light)"/>
          <stop offset="1" stop-color="var(--maroon)"/>
        </linearGradient>
      </defs>
      <path d="M0,380 C250,412 500,440 900,422 L900,470 L0,470 Z" fill="var(--gold)"/>
      <path d="M0,392 C250,424 500,452 900,432 L900,470 L0,470 Z" fill="url(#bandGradient)"/>
    </svg>

    <div class="brand">
      <span class="brand-mark"></span>
      <span class="brand-name">Blue Lantern</span>
      <span class="brand-sub">Financial Group</span>
    </div>

    <div class="person">
      <p class="person-name">Glen R. Whitmore</p>
      <p class="person-title">Managing Partner</p>
    </div>

    <div class="divider"></div>

    <ul class="contact">
      <li>4197-B West Harlow Creek Rd.</li>
      <li>Brenton Falls, OR 97481</li>
      <li><span class="contact-label">P :</span> 615-555-0148</li>
      <li><span class="contact-label">F :</span> 615-555-0192</li>
      <li><span class="contact-label">E :</span> glen.whitmore@bluelanternfinancialgroup.example</li>
      <li><span class="contact-label">W :</span> Bluelanternfinancialgroup.example</li>
    </ul>
  </div>
</body>
</html>
```